Business Card Design for Venture Kite

Venture Kite is a pro bono student consultancy service offered by Corvala KTRB to social start ups and enterprises. We provide consulting services with expertise in areas such as Marketing, IT, Business Strategy and Innovation.
I have attached\ the Venture Kite Logo here for your perusal.
Industry/Entity Type
Business
Contact Information for Business Card
Name: Ha Min Park Name: Thomas Leung
Role: Project Leader Role: Vice Project Leader
M:0477203941 M: 0479352806
E: ha-min.park@corvalaktrb.org E: thomas.leung@corvalaktrb.org
W: www.corvalaktrb.org W: www.corvalaktrb.org

```html
<!DOCTYPE html>
<html lang="en">
<head>
<meta charset="utf-8">
<title>Venture Kite – Business Card</title>
<link href="https://fonts.googleapis.com/css2?family=Oswald:wght@700&family=Jost:wght@400;600&family=Questrial&display=swap" rel="stylesheet">
<style>
  :root {
    --backdrop: #2b2b2d;
    --card-top: #ffffff;
    --card-bottom: #e9e9e9;
    --ink: #161616;
    --ink-soft: #333333;
    --accent: #ef8a0c;
    --accent-deep: #d97200;
    --base-band: #2e2e2e;
  }
  * { box-sizing: border-box; margin: 0; padding: 0; }
  html, body {
    width: 1200px; height: 997px; overflow: hidden;
    background: var(--backdrop);
  }
  .sheet {
    width: 1200px; height: 997px;
    display: flex; flex-direction: column;
    align-items: center; justify-content: center;
    gap: 44px;
  }
  .card {
    position: relative;
    width: 760px; height: 434px;
    background: linear-gradient(160deg, var(--card-top) 0%, var(--card-bottom) 100%);
    overflow: hidden;
    box-shadow: 0 10px 30px rgba(0,0,0,.45);
  }
  .card__base {
    position: absolute; left: 0; bottom: 0;
    width: 760px; height: 60px; display: block;
  }
  .wordmark {
    font-family: "Oswald", "Arial Narrow", sans-serif;
    font-weight: 700;
    color: var(--ink);
    letter-spacing: 1px;
    text-transform: uppercase;
    line-height: 1;
    white-space: nowrap;
  }
  .card--front .wordmark {
    position: absolute; left: 0; right: 0; top: 160px;
    text-align: center; font-size: 78px;
  }
  .card--back .wordmark {
    position: absolute; left: 0; right: 0; top: 58px;
    text-align: center; font-size: 54px;
  }
  .holder {
    position: absolute; right: 70px; top: 168px;
    text-align: right;
  }
  .holder__name {
    font-family: "Jost", "Futura", sans-serif;
    font-weight: 600; font-size: 22px;
    letter-spacing: 1px; color: var(--ink);
    text-transform: uppercase;
  }
  .holder__role {
    font-family: "Questrial", sans-serif;
    font-size: 13px; color: var(--ink-soft);
    margin-top: 2px;
  }
  .contact-tab {
    position: absolute; left: 0; top: 262px;
    width: 58px; height: 112px;
    background: var(--accent);
    border-radius: 0 12px 12px 0;
    display: flex; flex-direction: column;
    align-items: center; justify-content: space-around;
    padding: 8px 0;
  }
  .contact-tab svg { width: 20px; height: 20px; display: block; }
  .contact-list {
    position: absolute; left: 78px; top: 266px;
    list-style: none;
    font-family: "Questrial", sans-serif;
    font-size: 15px; color: var(--ink-soft);
    letter-spacing: .5px;
  }
  .contact-list li { height: 34px; line-height: 34px; }
</style>
</head>
<body>
<main class="sheet">

  <section class="card card--front" aria-label="Card front">
    <h1 class="wordmark">Venture Kite</h1>
    <svg class="card__base" viewBox="0 0 760 60" aria-hidden="true">
      <path d="M0 60 L0 52 L470 40 L760 40 L760 60 Z" fill="var(--base-band)"/>
      <path d="M462 42 C480 30 492 27 520 26 L760 12 L760 40 Z" fill="var(--accent)"/>
    </svg>
  </section>

  <section class="card card--back" aria-label="Card back">
    <h2 class="wordmark">Venture Kite</h2>

    <div class="holder">
      <p class="holder__name">Ha Min Park</p>
      <p class="holder__role">Project Leader</p>
    </div>

    <div class="contact-tab" aria-hidden="true">
      <svg viewBox="0 0 20 20"><rect x="5" y="1.5" width="10" height="17" rx="1.5" fill="none" stroke="#fff" stroke-width="1.6"/><line x1="8.5" y1="15.5" x2="11.5" y2="15.5" stroke="#fff" stroke-width="1.4"/></svg>
      <svg viewBox="0 0 20 20"><rect x="2" y="4.5" width="16" height="11" fill="none" stroke="#fff" stroke-width="1.6"/><path d="M2 4.5 L10 11 L18 4.5" fill="none" stroke="#fff" stroke-width="1.6"/></svg>
      <svg viewBox="0 0 20 20"><circle cx="10" cy="10" r="8" fill="none" stroke="#fff" stroke-width="1.6"/><ellipse cx="10" cy="10" rx="3.5" ry="8" fill="none" stroke="#fff" stroke-width="1.3"/><line x1="2" y1="10" x2="18" y2="10" stroke="#fff" stroke-width="1.3"/></svg>
    </div>

    <ul class="contact-list">
      <li class="contact-list__phone">0477203941</li>
      <li class="contact-list__email">ha-min.park@corvalaktrb.org</li>
      <li class="contact-list__web">www.corvalaktrb.org</li>
    </ul>

    <svg class="card__base" viewBox="0 0 760 60" aria-hidden="true">
      <path d="M0 60 L0 52 L470 40 L760 40 L760 60 Z" fill="var(--base-band)"/>
      <path d="M462 42 C480 30 492 27 520 26 L760 12 L760 40 Z" fill="var(--accent)"/>
    </svg>
  </section>

</main>
</body>
</html>
```